Bold Sparrow Studio
Business Cards, Stationary, T-Shirts
Bold Sparrow Studio -
Creative Brief
Use specific fonts
Feel free to use clear fonts
Bright & Fun-filled
Arch. Dave Tuazon
Business Development Manager
Level C, QRT Business Center 482 Willowgate Street Mandaluyong, Metro Manila
tuazon.ella@brightnestinteriors.com
Okay to use single colors in the background with a different color per sheet. Please make format easily editable to change the names and designations of the people on the business cards
Kitchens Closets Storage Solutions

```html
<!DOCTYPE html>
<html lang="en">
<head>
<meta charset="utf-8">
<title>Brightnest Interiors – Business Card</title>
<link href="https://fonts.googleapis.com/css2?family=Arimo:wght@400;700&display=swap" rel="stylesheet">
<style>
  :root{
    --page:#eeeae4;
    --card-white:#ffffff;
    --brand-blue:#1466b8;
    --band-top:#2f86d4;
    --band-bottom:#0d4f9c;
    --accent-green:#7cc242;
    --rule-grey:#d6d9dd;
    --ink:#1d1d1d;
    --band-ink:#ffffff;
    --mark-faint:#e9ebee;
  }
  *{box-sizing:border-box;margin:0;padding:0}
  html,body{width:1200px;height:965px;overflow:hidden}
  body{background:var(--page);font-family:"Arimo",Arial,sans-serif;position:relative}
  .card{
    position:absolute;left:213px;top:263px;width:774px;height:439px;
    background:var(--card-white);border-radius:30px;overflow:hidden;
    box-shadow:0 10px 24px rgba(0,0,0,.22);
  }
  .brand{
    position:absolute;left:28px;top:70px;width:320px;
    display:flex;flex-direction:column;align-items:center;gap:16px;
  }
  .brand-square{width:92px;height:92px;background:var(--brand-blue);border-radius:6px}
  .brand-name{
    color:var(--brand-blue);font-weight:700;font-size:30px;line-height:1.1;
    text-align:center;letter-spacing:.5px;
  }
  .faint-shape{
    position:absolute;left:490px;top:18px;width:150px;height:150px;
    background:var(--mark-faint);border-radius:50%;
  }
  .person{position:absolute;right:60px;top:104px;text-align:right}
  .person-name{color:var(--brand-blue);font-size:29px;font-weight:400}
  .person-title{color:var(--ink);font-size:19px;margin-top:8px}
  .rules{position:absolute;left:0;top:263px;width:100%}
  .rule-grey{height:2px;background:var(--rule-grey)}
  .rule-green{height:4px;background:var(--accent-green);margin-top:3px}
  .band{
    position:absolute;left:0;top:278px;width:100%;height:161px;
    background:linear-gradient(180deg,var(--band-top),var(--band-bottom));
    color:var(--band-ink);
  }
  .address{
    position:absolute;right:450px;top:33px;text-align:right;
    font-size:18px;line-height:31px;
  }
  .divider{position:absolute;left:344px;top:30px;width:1px;height:100px;background:rgba(255,255,255,.7)}
  .contacts{position:absolute;left:362px;top:33px;list-style:none;font-size:18px;line-height:31px}
  .contacts li{display:flex;align-items:center;gap:10px}
  .contact-icon{width:18px;height:18px;flex:none;display:flex;align-items:center;justify-content:center;font-size:17px}
</style>
</head>
<body>
  <div class="card">
    <div class="brand">
      <div class="brand-square"></div>
      <div class="brand-name">BRIGHTNEST<br>INTERIORS, INC</div>
    </div>
    <div class="faint-shape"></div>
    <div class="person">
      <div class="person-name">Arch. Dave Tuazon</div>
      <div class="person-title">Business Development Manager</div>
    </div>
    <div class="rules">
      <div class="rule-grey"></div>
      <div class="rule-green"></div>
    </div>
    <div class="band">
      <div class="address">
        Level C, QRT Business Center<br>
        482 Willowgate Street<br>
        Mandaluyong, Metro Manila
      </div>
      <div class="divider"></div>
      <ul class="contacts">
        <li>
          <span class="contact-icon">
            <svg width="16" height="16" viewBox="0 0 24 24" fill="#fff"><path d="M6.6 10.8a15.1 15.1 0 0 0 6.6 6.6l2.2-2.2c.3-.3.7-.4 1-.2 1.1.4 2.3.6 3.6.6.6 0 1 .4 1 1V20c0 .6-.4 1-1 1A17 17 0 0 1 3 4c0-.6.4-1 1-1h3.5c.6 0 1 .4 1 1 0 1.3.2 2.5.6 3.6.1.3 0 .7-.2 1z"/></svg>
          </span>(632) 555-0148
        </li>
        <li>
          <span class="contact-icon">
            <svg width="16" height="16" viewBox="0 0 24 24" fill="#fff"><rect x="6" y="2" width="12" height="7"/><rect x="3" y="10" width="18" height="8" rx="1"/><rect x="6" y="15" width="12" height="7" fill="#fff" stroke="#1a5fae" stroke-width="1.5"/></svg>
          </span>(632) 555-0172
        </li>
        <li><span class="contact-icon">@</span>tuazon.ella@brightnestinteriors.com</li>
      </ul>
    </div>
  </div>
</body>
</html>
```